brightmesh Business Card

Already have the logo, but now need the business card design

Industry/Entity Type

Business Software

Contact Information for Business Card

web site will be brightmesh.io / The card should have the person name / position / mobile / email / and company address

Colors

Designer to choose colors to be used in the design.

Requirements
Must have
• See business card details
• One side to have the brightmesh logo
Nice to have
• If possible the 'O' from flow can be watermarked into the second side
• Try to fit in the words brightmesh Business Solutions

```html
<!DOCTYPE html>
<html lang="en">
<head>
<meta charset="utf-8">
<title>brightmesh Business Card</title>
<link rel="stylesheet" href="https://fonts.googleapis.com/css2?family=Lato:wght@400;700&family=Montserrat:wght@500&display=swap">
<style>
  :root {
    --backdrop: #262628;
    --card: #1e1f21;
    --card-edge: #2b2c2f;
    --grey-strong: #8e8f92;
    --grey-soft: #7a7b7e;
    --rule: #4a4b4e;
    --icon-bg: #6f7073;
    --accent: #e1141f;
  }
  * { margin: 0; padding: 0; box-sizing: border-box; }
  html, body { width: 1200px; height: 1108px; overflow: hidden; }
  body {
    background: var(--backdrop);
    font-family: "Lato", sans-serif;
    position: relative;
  }
  .card {
    position: absolute;
    top: 224px;
    width: 380px;
    height: 660px;
    border-radius: 22px;
    background: var(--card);
    border: 1px solid var(--card-edge);
    box-shadow: 0 18px 40px rgba(0,0,0,0.45);
    overflow: hidden;
  }
  .card--front { left: 180px; }
  .card--back { left: 640px; }

  .front__brand { position: absolute; top: 150px; width: 100%; text-align: center; }
  .front__wordmark {
    font-family: "Lato", sans-serif;
    font-weight: 400;
    font-size: 60px;
    letter-spacing: -1px;
    color: var(--grey-strong);
    line-height: 1;
  }
  .front__tagline {
    font-family: "Montserrat", sans-serif;
    font-weight: 500;
    font-size: 21px;
    letter-spacing: 0.5px;
    color: var(--grey-strong);
    margin-top: 6px;
  }
  .person { position: absolute; top: 340px; width: 100%; text-align: center; }
  .person__name {
    font-weight: 700;
    font-size: 23px;
    letter-spacing: 0.5px;
    color: var(--grey-strong);
  }
  .person__surname { color: var(--accent); }
  .person__role { font-size: 17px; color: var(--grey-soft); margin-top: 2px; }

  .contact-icons {
    position: absolute; top: 418px; left: 50%;
    transform: translateX(-50%);
    display: flex; align-items: center; gap: 6px;
  }
  .contact-icons__rule { width: 70px; height: 1px; background: var(--rule); }
  .contact-icons svg { width: 24px; height: 24px; display: block; }

  .contact { position: absolute; top: 458px; width: 100%; text-align: center; color: var(--grey-soft); font-size: 18px; line-height: 26px; }
  .contact__divider { width: 190px; height: 1px; background: var(--rule); margin: 8px auto; }

  .back__pattern {
    position: absolute; inset: 0 0 180px 0;
    background: linear-gradient(180deg, #2c2d30 0%, #232427 60%, var(--card) 100%);
  }
  .back__wordmark {
    position: absolute; left: 90px; top: 520px;
    font-weight: 400;
    font-size: 58px;
    letter-spacing: -1px;
    color: var(--accent);
    line-height: 1;
  }
</style>
</head>
<body>
  <section class="card card--front">
    <div class="front__brand">
      <div class="front__wordmark">brightmesh</div>
      <div class="front__tagline">BUSINESS SOLUTIONS</div>
    </div>
    <div class="person">
      <div class="person__name">DANIEL <span class="person__surname">CARTER</span></div>
      <div class="person__role">Managing Director</div>
    </div>
    <div class="contact-icons">
      <span class="contact-icons__rule"></span>
      <svg viewBox="0 0 24 24" aria-label="phone">
        <circle cx="12" cy="12" r="12" fill="var(--icon-bg)"/>
        <path d="M8.5 6.5l2 2-1.2 1.5c.8 1.7 2 2.9 3.7 3.7l1.5-1.2 2 2-1.5 1.8c-3.8-.6-7.4-4.2-8-8z" fill="#1e1f21"/>
      </svg>
      <svg viewBox="0 0 24 24" aria-label="email">
        <circle cx="12" cy="12" r="12" fill="var(--icon-bg)"/>
        <rect x="6.5" y="8" width="11" height="8" fill="#1e1f21"/>
        <path d="M6.5 8l5.5 4.5L17.5 8" fill="none" stroke="var(--icon-bg)" stroke-width="1.2"/>
      </svg>
      <svg viewBox="0 0 24 24" aria-label="address">
        <circle cx="12" cy="12" r="12" fill="var(--icon-bg)"/>
        <path d="M12 5.5a4 4 0 0 0-4 4c0 3 4 8 4 8s4-5 4-8a4 4 0 0 0-4-4z" fill="#1e1f21"/>
        <circle cx="12" cy="9.5" r="1.5" fill="var(--icon-bg)"/>
      </svg>
      <span class="contact-icons__rule"></span>
    </div>
    <div class="contact">
      <div>044-987 654 321</div>
      <div>hello@brightmesh.io</div>
      <div>www.brightmesh.io</div>
      <div class="contact__divider"></div>
      <div>17, Harbour Street</div>
      <div>Northland, 30218</div>
    </div>
  </section>

  <section class="card card--back">
    <div class="back__pattern" role="img" aria-label="Faint repeating brand-mark watermark pattern"></div>
    <div class="back__wordmark">brightmesh</div>
  </section>
</body>
</html>
```